Funny Images Website required

I need a web design for a new funny images posting website, The name will be QOVIBLANTA, My plan is to post two sets of photos per day each set with approx 10-15 photos, funny images from around the web, people can share the albums or individual photos to Pictorama, zindle, chirpex, I'll also be posting videos from around the web, I would like the design to be international and fun, perhaps all the flags from the American continent? Will also need a Pictorama fan page where I can post one photo per set which will include a link to my site, with time I plan on adding advertisements and more and more visitors to my page, the design for QOVIBLANTA logo I would like to follow wobblefunnel.example and gigglevault.example for example but not in any way copy them
Updates

Hi, I'm reviewing all the designs sent, just a friendly reminder website should have the following: From top to bottom of page 1) Search option 1.1) Place for banner and ads 1,2) place for Pictorama likes and counter of how many likes 2) Sign in + Remember my details (for easy access) 3) Sign up 4) Bar with "photos" "upload" "Videos" "Categories" "your profile" "Popular" 5) Date next to each album when it's posted, each album to have a Pictorama like and Share option 6) Galleries of videos and photos in a column going down and on the right hand side options for ads, top galleries, or you might like albums 7) at the bottom of the page, pages 1, 2, 3 etc as the galleries will continue 8) Contact info, disclaimer / copyright, etc. I'm not a graphic designer or expert on this so thanks for bearing with me and your designs I like all of them but can only choose one so I'm in the process of choosing one. thanks Qo

Target Market(s)

Latin America audience and people in the USA, ages 14-40

Coding

Coded - Design and coding required

Colors
f37122
0393ce

Requirements
Must have
• likes on Pictorama, share option to Pictorama, log in & sign up option, upload photo option, place for advertisement,

```html
<!DOCTYPE html>
<html lang="en">
<head>
<meta charset="utf-8">
<title>QOVIBLANTA – Funny Images</title>
<link href="https://fonts.googleapis.com/css2?family=Open+Sans:wght@400;600;700;800&display=swap" rel="stylesheet">
<style>
:root{
  --black:#000;
  --ink:#222;
  --muted:#8a8a8a;
  --line:#e4e4e4;
  --accent:#f37122;
  --blue:#0393ce;
  --white:#fff;
  --footer-bar:#151515;
  --panel:#fff;
  --ad:#f2f2f2;
}
*{box-sizing:border-box;margin:0;padding:0}
html,body{width:1200px;height:4176px;overflow:hidden}
body{background:var(--black);font-family:"Open Sans",Arial,sans-serif;color:var(--ink);position:relative}
.abs{position:absolute}
.top-rule{left:0;top:0;width:1200px;height:4px;background:var(--accent)}
.logo{left:56px;top:34px;font-size:32px;font-weight:800;color:var(--white);letter-spacing:1px;line-height:40px}
.contact-top{left:941px;top:30px;color:#ddd;font-size:12px;line-height:22px}
/* account */
.account{left:410px;top:22px;display:flex;gap:8px;align-items:center}
.account .in{width:138px;height:30px;border:1px solid #444;background:#111;color:#999;font-size:11px;line-height:28px;padding-left:10px}
.account .signin{height:30px;padding:0 14px;background:var(--accent);color:#fff;font-size:11px;font-weight:700;line-height:30px;text-transform:uppercase}
.account .signup{height:30px;padding:0 14px;background:var(--blue);color:#fff;font-size:11px;font-weight:700;line-height:30px;text-transform:uppercase}
.remember{left:410px;top:62px;display:flex;align-items:center;gap:7px;font-size:11px;color:#bbb}
.remember i{width:12px;height:12px;border:1px solid #777;display:block;background:#111;position:relative}
.remember i:after{content:"";position:absolute;left:3px;top:0;width:4px;height:7px;border-right:2px solid var(--accent);border-bottom:2px solid var(--accent);transform:rotate(40deg)}
.panel{left:56px;top:103px;width:1088px;height:3717px;background:var(--panel)}
/* nav */
.nav{left:75px;top:113px;height:46px;display:flex;align-items:center;font-size:12px;font-weight:600;text-transform:uppercase}
.nav a{color:var(--ink);text-decoration:none;padding:0 15px;height:46px;line-height:46px}
.nav a.active{background:var(--accent);color:var(--white)}
.nav a.upload{background:var(--blue);color:var(--white);margin-left:12px;display:flex;align-items:center;gap:7px}
.search{left:827px;top:113px;width:298px;height:46px;display:flex}
.search .field{flex:1;background:var(--black);color:#bbb;font-size:12px;line-height:46px;padding-left:14px;display:flex;align-items:center;gap:8px}
.search .btn{width:78px;background:var(--accent);color:var(--white);font-weight:700;font-size:12px;text-align:center;line-height:46px}
/* photos */
.ph{position:absolute}
.hero{left:75px;top:175px;width:1050px;height:518px;background:linear-gradient(90deg,#b08060 0%,#d7c8b8 35%,#e9eef2 60%,#cfd8e2 100%)}
.arrow{top:702px;width:53px;height:128px;background:var(--accent);display:flex;align-items:center;justify-content:center}
.thumb{top:702px;width:173px;height:128px}
/* sections */
.tag{display:flex;height:42px;align-items:stretch}
.tag .sq{width:31px;background:var(--accent);display:flex;align-items:center;justify-content:center}
.tag .lbl{background:var(--black);color:var(--white);font-size:11px;font-weight:700;text-transform:uppercase;padding:0 14px;line-height:42px}
.post-title{font-size:16px;font-weight:600;text-transform:uppercase;color:var(--ink);letter-spacing:.2px}
.meta{font-size:11px;color:var(--muted)}
.shadowed{box-shadow:0 14px 14px -8px rgba(0,0,0,.35)}
.share{display:flex;align-items:center;width:708px;font-size:12px;font-weight:600}
.share .icons{display:flex;gap:8px;margin-left:16px}
.share .icons span{width:38px;height:38px;border:1.5px solid #cfcfcf;border-radius:50%;display:block}
.share .like{margin-left:22px;display:flex;align-items:center;height:26px;font-size:11px}
.share .like b{background:var(--blue);color:#fff;padding:0 10px;line-height:26px;font-weight:700}
.share .like em{font-style:normal;border:1px solid #cfcfcf;border-left:0;padding:0 9px;line-height:24px;color:var(--ink)}
.share .comments{margin-left:auto;display:flex;align-items:center;gap:8px;font-size:12px}
.divider{height:1px;background:var(--line)}
.play{position:absolute;left:50%;top:50%;width:92px;height:92px;margin:-46px 0 0 -46px;border-radius:50%;border:5px solid rgba(255,255,255,.85);background:rgba(0,0,0,.25)}
.play:after{content:"";position:absolute;left:34px;top:22px;border-left:30px solid #fff;border-top:19px solid transparent;border-bottom:19px solid transparent}
.play.sm{width:40px;height:40px;margin:-20px 0 0 -20px;border-width:3px}
.play.sm:after{left:14px;top:9px;border-left-width:13px;border-top-width:8px;border-bottom-width:8px}
.card-title{font-size:12px;font-weight:700;text-transform:uppercase;line-height:17px}
.card-text{font-size:10px;color:var(--muted);line-height:14px}
/* sidebar */
.side-h{font-size:13px;font-weight:700;text-transform:uppercase}
.side-cap{font-size:10px;text-transform:uppercase;color:var(--ink)}
.side-sub{font-size:9px;color:var(--muted)}
.news{display:flex;gap:26px}
.news .nt{font-size:12px;font-weight:700}
.news p{font-size:10px;color:#666;line-height:14px;margin-top:4px;width:188px}
.ad-box{background:var(--ad);border:1px dashed #cfcfcf;display:flex;flex-direction:column;align-items:center;justify-content:center;color:#aaa;font-size:11px;text-transform:uppercase;letter-spacing:1px;gap:6px}
.ad-box b{font-size:13px;color:#999}
.fans{border:1px solid var(--line);padding:18px}
.fans .row{display:flex;align-items:center;gap:10px}
.fans .dot{width:34px;height:34px;border-radius:50%;background:var(--blue)}
.fans .name{font-size:13px;font-weight:700}
.fans .count{font-size:11px;color:var(--muted)}
.fans .btn{margin-top:14px;height:32px;background:var(--blue);color:#fff;font-size:12px;font-weight:700;text-align:center;line-height:32px;text-transform:uppercase}
.toplist{font-size:12px;line-height:30px}
.toplist div{border-bottom:1px solid var(--line);display:flex;justify-content:space-between}
.toplist span{color:var(--accent);font-weight:700}
/* pagination */
.pager{left:78px;top:3733px;display:flex;gap:10px;font-size:11px;font-weight:600}
.pager span{height:37px;line-height:37px;background:#eee;text-align:center;min-width:37px;padding:0 10px}
.pager .on{background:var(--accent);color:#fff}
.pager .next{margin-left:30px}
/* footer */
.f-h{font-size:15px;font-weight:700;color:var(--white);text-transform:uppercase}
.f-links{font-size:12px;color:#ccc;line-height:26px}
.f-about b{display:block;color:#fff;font-size:12px;margin-bottom:8px}
.f-about p{font-size:11px;color:#aaa;line-height:15px;width:330px;margin-bottom:10px}
.socials{display:flex;gap:8px}
.socials span{width:34px;height:34px;border-radius:50%;display:block}
.talk{font-size:12px;color:#ccc;line-height:22px}
.talk div{display:flex;align-items:center;gap:8px}
.input{width:203px;height:36px;border:1px solid #555;background:var(--black);color:#ddd;font-size:12px;line-height:34px;padding-left:10px}
.subscribe{width:203px;height:34px;background:var(--accent);color:#fff;font-weight:700;font-size:12px;text-align:center;line-height:34px}
.bottom-bar{left:0;top:4093px;width:1200px;height:83px;background:var(--footer-bar)}
.copyright{left:56px;top:4126px;font-size:11px;color:#bbb}
.copyright em{font-style:normal;color:var(--accent)}
.bottom-links{left:650px;top:4126px;font-size:11px;color:#999;width:490px;text-align:right;text-transform:uppercase;letter-spacing:.3px}
</style>
</head>
<body>
<div class="abs top-rule"></div>
<div class="abs logo">QOVIBLANTA</div>

<div class="abs account">
  <div class="in">Username</div>
  <div class="in">Password</div>
  <div class="signin">Sign in</div>
  <div class="signup">Sign up</div>
</div>
<div class="abs remember"><i></i>Remember my details</div>

<div class="abs contact-top">Phone: 555 014 2238<br>Email: support@qoviblanta.example</div>

<div class="abs panel"></div>

<nav class="abs nav">
  <a class="active">Home</a><a>Photos</a><a>Videos</a><a>Categories</a><a>Popular</a><a>Your Profile</a>
  <a class="upload"><svg width="12" height="12" viewBox="0 0 12 12"><path d="M6 1 L6 9 M2.5 4.5 L6 1 L9.5 4.5 M1 11 L11 11" fill="none" stroke="#fff" stroke-width="1.6"/></svg>Upload</a>
</nav>
<div class="abs search">
  <div class="field"><svg width="12" height="12" viewBox="0 0 12 12"><circle cx="5" cy="5" r="3.8" fill="none" stroke="#fff" stroke-width="1.5"/><line x1="8" y1="8" x2="11" y2="11" stroke="#fff" stroke-width="1.5"/></svg>Enter any keywords...</div>
  <div class="btn">SEARCH</div>
</div>

<div class="ph hero" role="img" aria-label="Featured photo of a smiling woman outside a white building"></div>
<div class="abs arrow" style="left:75px"><svg width="16" height="24" viewBox="0 0 16 24"><path d="M12 3 L4 12 L12 21" fill="none" stroke="#fff" stroke-width="4"/></svg></div>
<div class="abs arrow" style="left:1072px"><svg width="16" height="24" viewBox="0 0 16 24"><path d="M4 3 L12 12 L4 21" fill="none" stroke="#fff" stroke-width="4"/></svg></div>
<div class="ph thumb" style="left:139px;background:linear-gradient(135deg,#7d8fa3,#c9c2b6)" role="img" aria-label="Video thumbnail: friends outdoors"><span class="play sm"></span></div>
<div class="ph thumb" style="left:326px;background:linear-gradient(135deg,#d9b48f,#f0e2cf)" role="img" aria-label="Photo thumbnail: woman laughing"></div>
<div class="ph thumb" style="left:512px;background:linear-gradient(135deg,#555,#d8d8d8)" role="img" aria-label="Photo thumbnail: black and white portrait"></div>
<div class="ph thumb" style="left:699px;background:linear-gradient(135deg,#e7e2d8,#9c8a72)" role="img" aria-label="Video thumbnail: man relaxing"><span class="play sm"></span></div>
<div class="ph thumb" style="left:885px;background:linear-gradient(135deg,#8a3e3a,#e0a898)" role="img" aria-label="Photo thumbnail: couple together"></div>

<div class="abs" style="left:804px;top:880px;width:1px;height:2860px;background:var(--line)"></div>

<!-- post 1 -->
<div class="abs tag" style="left:72px;top:905px"><span class="sq"><svg width="14" height="12"><rect x="1" y="2" width="12" height="9" fill="none" stroke="#fff" stroke-width="1.5"/></svg></span><span class="lbl">Photo Sets</span></div>
<div class="abs post-title" style="left:72px;top:970px">Sed ut perspiciatis unde omnis iste natus error</div>
<div class="abs meta" style="left:72px;top:998px">Submitted by lorenvasquez on Mon, 2013-05-20 18:48</div>
<div class="ph shadowed" style="left:78px;top:1036px;width:702px;height:337px;background:linear-gradient(120deg,#3a2a55,#b0506e 45%,#e9c29a 70%,#5a3a68)" role="img" aria-label="Party photo of friends dancing under club lights"></div>
<div class="abs share" style="left:72px;top:1406px">Share With Us<div class="icons"><span></span><span></span><span></span><span></span></div><div class="like"><b>Like</b><em>1,248</em></div><div class="comments"><svg width="20" height="16"><rect x="0" y="2" width="14" height="10" rx="2" fill="#f37122"/><rect x="6" y="5" width="14" height="10" rx="2" fill="#f37122" stroke="#fff"/></svg>23 Comments</div></div>
<div class="abs divider" style="left:72px;top:1467px;width:713px"></div>

<!-- post 2 -->
<div class="abs tag" style="left:72px;top:1506px"><span class="sq"><svg width="14" height="12"><rect x="1" y="2" width="9" height="8" fill="#fff"/><path d="M10 6 L14 3 L14 10 Z" fill="#fff"/></svg></span><span class="lbl">Our Videos</span></div>
<div class="abs post-title" style="left:72px;top:1573px">Sed ut perspiciatis unde omnis iste natus error</div>
<div class="abs meta" style="left:72px;top:1601px">Submitted by lorenvasquez on Mon, 2013-05-20 18:48</div>
<div class="ph shadowed" style="left:78px;top:1643px;width:702px;height:328px;background:linear-gradient(160deg,#6fa6d8,#bcd8ee 50%,#c24a55 75%,#5d7a3a)" role="img" aria-label="Video still of two people jumping against a blue sky"><span class="play"></span></div>
<div class="abs share" style="left:72px;top:2011px">Share With Us<div class="icons"><span></span><span></span><span></span><span></span></div><div class="like"><b>Like</b><em>986</em></div><div class="comments"><svg width="20" height="16"><rect x="0" y="2" width="14" height="10" rx="2" fill="#f37122"/><rect x="6" y="5" width="14" height="10" rx="2" fill="#f37122" stroke="#fff"/></svg>23 Comments</div></div>
<div class="abs divider" style="left:72px;top:2068px;width:713px"></div>

<!-- post 3 -->
<div class="abs tag" style="left:72px;top:2105px"><span class="sq"><svg width="14" height="12"><rect x="1" y="2" width="12" height="9" fill="none" stroke="#fff" stroke-width="1.5"/></svg></span><span class="lbl">Photo Sets</span></div>
<div class="abs post-title" style="left:72px;top:2169px">Sed ut perspiciatis unde omnis iste natus error</div>
<div class="abs meta" style="left:72px;top:2197px">Submitted by lorenvasquez on Mon, 2013-05-20 18:48</div>
<div class="ph shadowed" style="left:78px;top:2236px;width:208px;height:175px;background:linear-gradient(135deg,#2a2420,#d7b59a 60%,#f1e3d4)" role="img" aria-label="Photo of a woman lying down"></div>
<div class="ph shadowed" style="left:320px;top:2236px;width:208px;height:175px;background:linear-gradient(180deg,#1e2a40,#5a6a88 55%,#c8a070)" role="img" aria-label="City skyline at dusk"></div>
<div class="ph shadowed" style="left:562px;top:2236px;width:208px;height:175px;background:linear-gradient(135deg,#7a5a3a,#e8c48a 55%,#f4e7d0)" role="img" aria-label="Photo of a woman with sunglasses"></div>
<div class="abs" style="left:72px;top:2436px;width:214px"><div class="card-title">65 Beauty tips &amp; tricks every woman...</div><div class="card-text" style="margin-top:10px">Hi Everyone! We are proud to show you the launch of our new.</div></div>
<div class="abs" style="left:316px;top:2436px;width:214px"><div class="card-title">65 Beauty tips &amp; tricks every woman...</div><div class="card-text" style="margin-top:10px">Hi Everyone! We are proud to show you the launch of our new.</div></div>
<div class="abs" style="left:560px;top:2436px;width:214px"><div class="card-title">65 Beauty tips &amp; tricks every woman...</div><div class="card-text" style="margin-top:10px">Hi Everyone! We are proud to show you the launch of our new.</div></div>
<div class="abs divider" style="left:72px;top:2556px;width:713px"></div>

<!-- post 4 -->
<div class="abs tag" style="left:72px;top:2589px"><span class="sq"><svg width="14" height="12"><rect x="1" y="2" width="9" height="8" fill="#fff"/><path d="M10 6 L14 3 L14 10 Z" fill="#fff"/></svg></span><span class="lbl">Our Videos</span></div>
<div class="abs post-title" style="left:72px;top:2653px">Sed ut perspiciatis unde omnis iste natus error</div>
<div class="abs meta" style="left:72px;top:2681px">Submitted by lorenvasquez on Mon, 2013-05-20 18:48</div>
<div class="ph shadowed" style="left:78px;top:2723px;width:702px;height:334px;background:linear-gradient(100deg,#6a5a4a,#d9b38a 40%,#e8e4dc 60%,#3a3330)" role="img" aria-label="Video still of friends shopping together"><span class="play"></span></div>
<div class="abs share" style="left:72px;top:3091px">Share With Us<div class="icons"><span></span><span></span><span></span><span></span></div><div class="like"><b>Like</b><em>2,305</em></div><div class="comments"><svg width="20" height="16"><rect x="0" y="2" width="14" height="10" rx="2" fill="#f37122"/><rect x="6" y="5" width="14" height="10" rx="2" fill="#f37122" stroke="#fff"/></svg>23 Comments</div></div>
<div class="abs divider" style="left:72px;top:3154px;width:713px"></div>

<!-- post 5 -->
<div class="abs tag" style="left:72px;top:3182px"><span class="sq"><svg width="14" height="12"><rect x="1" y="2" width="12" height="9" fill="none" stroke="#fff" stroke-width="1.5"/></svg></span><span class="lbl">Our Gallery</span></div>
<div class="abs post-title" style="left:72px;top:3249px">Sed ut perspiciatis unde omnis iste natus error</div>
<div class="abs meta" style="left:72px;top:3277px">Submitted by lorenvasquez on Mon, 2013-05-20 18:48</div>
<div class="ph" style="left:78px;top:3316px;width:167px;height:120px;background:linear-gradient(135deg,#1a2a6a,#7a8ae0)" role="img" aria-label="Concert crowd"></div>
<div class="ph" style="left:256px;top:3316px;width:167px;height:120px;background:linear-gradient(135deg,#e8d4a8,#b08850)" role="img" aria-label="Woman on the beach"></div>
<div class="ph" style="left:434px;top:3316px;width:167px;height:120px;background:linear-gradient(135deg,#8ab070,#efd9b8)" role="img" aria-label="Friends outdoors"></div>
<div class="ph" style="left:612px;top:3316px;width:167px;height:120px;background:linear-gradient(135deg,#6a4a30,#e0b890)" role="img" aria-label="Group of friends"></div>
<div class="ph" style="left:78px;top:3447px;width:167px;height:120px;background:linear-gradient(135deg,#cfd8e0,#8a9aa8)" role="img" aria-label="Hands holding a phone"></div>
<div class="ph" style="left:256px;top:3447px;width:167px;height:120px;background:linear-gradient(135deg,#e0e0e0,#8a6a5a)" role="img" aria-label="Group posing"></div>
<div class="ph" style="left:434px;top:3447px;width:167px;height:120px;background:linear-gradient(135deg,#3a2a2a,#c08070)" role="img" aria-label="Party snapshot"></div>
<div class="ph" style="left:612px;top:3447px;width:167px;height:120px;background:linear-gradient(135deg,#d8c8b8,#9a7050)" role="img" aria-label="Portrait outdoors"></div>
<div class="abs share" style="left:72px;top:3597px">Share With Us<div class="icons"><span></span><span></span><span></span><span></span></div><div class="like"><b>Like</b><em>764</em></div><div class="comments"><svg width="20" height="16"><rect x="0" y="2" width="14" height="10" rx="2" fill="#f37122"/><rect x="6" y="5" width="14" height="10" rx="2" fill="#f37122" stroke="#fff"/></svg>23 Comments</div></div>
<div class="abs divider" style="left:72px;top:3670px;width:713px"></div>

<div class="abs pager"><span class="on">1</span><span>2</span><span>3</span><span class="next">NEXT</span></div>

<!-- sidebar -->
<div class="abs tag" style="left:827px;top:905px"><span class="sq"><svg width="14" height="12"><rect x="1" y="2" width="12" height="9" fill="none" stroke="#fff" stroke-width="1.5"/></svg></span><span class="lbl">See the complete portfolio</span></div>
<div class="abs side-h" style="left:829px;top:970px">Our Blog News</div>
<div class="ph shadowed" style="left:830px;top:1011px;width:292px;height:153px;background:linear-gradient(135deg,#3a5a7a,#9ac0d8 55%,#c09070)" role="img" aria-label="Couple sitting by the water"></div>
<div class="abs side-cap" style="left:829px;top:1187px">Sed ut perspiciatia</div>
<div class="abs side-sub" style="left:829px;top:1207px">Sed ut perspiciatis unde omnis</div>
<div class="ph shadowed" style="left:830px;top:1244px;width:292px;height:154px;background:linear-gradient(135deg,#2a1a1a,#c05060 50%,#e8b8a0)" role="img" aria-label="Woman relaxing in a red top"></div>
<div class="abs side-cap" style="left:829px;top:1421px">Sed ut perspiciatia</div>
<div class="abs side-sub" style="left:829px;top:1441px">Sed ut perspiciatis unde omnis</div>
<div class="abs divider" style="left:827px;top:1484px;width:298px"></div>

<div class="abs side-h" style="left:829px;top:1507px">Latest News</div>
<div class="abs news" style="left:830px;top:1545px"><div style="width:78px;height:70px;background:linear-gradient(135deg,#8ab0d0,#e0b080)" role="img" aria-label="Beach news photo"></div><div><div class="nt">Lorem ipsum</div><p>A skin color switcher can also be used to customize the look of.</p></div></div>
<div class="abs news" style="left:830px;top:1645px"><div style="width:78px;height:70px;background:linear-gradient(135deg,#2a3a6a,#c8d0e8)" role="img" aria-label="City news photo"></div><div><div class="nt">Lorem ipsum</div><p>A skin color switcher can also be used to customize the look of.</p></div></div>
<div class="abs news" style="left:830px;top:1748px"><div style="width:78px;height:70px;background:linear-gradient(135deg,#222,#bbb)" role="img" aria-label="Black and white news photo"></div><div><div class="nt">Lorem ipsum</div><p>A skin color switcher can also be used to customize the look of.</p></div></div>
<div class="abs divider" style="left:827px;top:1854px;width:298px"></div>

<div class="abs side-h" style="left:829px;top:1886px">Our Videos</div>
<div class="ph shadowed" style="left:830px;top:1929px;width:292px;height:209px;background:linear-gradient(135deg,#f0e8dc,#d8a870 55%,#7a5a40)" role="img" aria-label="Video still of a woman with sunglasses"><span class="play sm"></span></div>
<div class="ph shadowed" style="left:830px;top:2177px;width:292px;height:209px;background:linear-gradient(180deg,#8ab8e0,#c8c8c8 55%,#5a5a5a)" role="img" aria-label="Video still of a city street with tall buildings"><span class="play sm"></span></div>
<div class="abs divider" style="left:827px;top:2420px;width:298px"></div>

<div class="abs side-h" style="left:829px;top:2446px">Pictorama Fans</div>
<div class="abs fans" style="left:827px;top:2484px;width:298px">
  <div class="row"><span class="dot"></span><div><div class="name">QOVIBLANTA</div><div class="count">12,480 people like this</div></div></div>
  <div class="btn">Like on Pictorama</div>
</div>

<div class="abs side-h" style="left:829px;top:2650px">Advertisement</div>
<div class="abs ad-box" style="left:827px;top:2688px;width:298px;height:250px"><b>300 × 250</b>Ad space</div>

<div class="abs side-h" style="left:829px;top:2980px">Top Galleries</div>
<div class="abs toplist" style="left:827px;top:3014px;width:298px">
  <div>Funny pets of the week<span>4.2k</span></div>
  <div>Epic fails compilation<span>3.8k</span></div>
  <div>Best of summer 2014<span>3.1k</span></div>
  <div>Office moments<span>2.6k</span></div>
  <div>Street art surprises<span>2.2k</span></div>
</div>

<div class="abs side-h" style="left:829px;top:3210px">Advertisement</div>
<div class="abs ad-box" style="left:827px;top:3248px;width:298px;height:420px"><b>300 × 420</b>Ad space</div>

<!-- footer -->
<div class="abs f-h" style="left:56px;top:3855px">Quick Links</div>
<div class="abs f-links" style="left:56px;top:3892px">Services<br>Contact Us<br>Privacy Policy<br>Terms &amp; Conditions<br>Disclaimer</div>

<div class="abs f-h" style="left:298px;top:3855px">About Us</div>
<div class="abs f-about" style="left:298px;top:3892px"><b>Lorem ipsum dolor sit amet</b><p>Ut wisi enim ad minim veniam, quis nostrud exerci tation ut wisi enim ad minim veniam, quis nostrud exerci tation</p><p>Ut wisi enim ad minim veniam, quis nostrud exerci ut wisi enim ad minim veniam, quis nostrud......</p></div>

<div class="abs f-h" style="left:699px;top:3855px">Follow Us</div>
<div class="abs socials" style="left:699px;top:3892px">
  <span style="background:var(--blue)" title="Pictorama"></span><span style="background:var(--accent)" title="zindle"></span><span style="background:var(--blue)" title="chirpex"></span><span style="background:var(--accent)" title="Share"></span>
</div>
<div class="abs f-h" style="left:699px;top:3960px">Talk To Us</div>
<div class="abs talk" style="left:699px;top:3993px">
  <div><svg width="14" height="14" viewBox="0 0 14 14"><path d="M3 1 L5 4 L4 6 Q6 9 8 10 L10 9 L13 11 L11 13 Q5 13 1 3 Z" fill="#fff"/></svg>555 010 7788</div>
  <div><svg width="14" height="10" viewBox="0 0 14 10"><rect x="0.5" y="0.5" width="13" height="9" fill="none" stroke="#fff"/><path d="M1 1 L7 6 L13 1" fill="none" stroke="#fff"/></svg>info@qoviblanta.example</div>
</div>

<div class="abs f-h" style="left:941px;top:3855px">Newsletter</div>
<div class="abs input" style="left:941px;top:3898px">Name:</div>
<div class="abs input" style="left:941px;top:3945px">Email</div>
<div class="abs subscribe" style="left:941px;top:4003px">SUBSCRIBE</div>

<div class="abs bottom-bar"></div>
<div class="abs copyright">Copyright © 2014 <em>QOVIBLANTA</em> all copyrights are reserved</div>
<div class="abs bottom-links">Home / About Us / Services / Gallery / Blog / Testimonials / Contact Us</div>
</body>
</html>
```